Lumex.CI Portal Application Design

** See the attached treatment PDF document with complete details, but here are the broad points:**

We need designs for a login screen and three very similar interior page screens. Because the app requires a CodeNest, RepoKeep or Stackpail account to login, screen shots are attached to this treatment. Please review those for the designs needed.
- Login Page
- Project Index page (with sidebar tabs for other options. Those specific pages do not need to be coded once we have the template).
- Project build list. A list of the builds available per project
- Build details. This shows the build steps and results of the build steps.

The site should be visually compatible with https://lumexweb.example-host.net. The same logo and color scheme (logo attached)

General templates are desired that we can build on.

There is a significant bonus tip involved if you’re willing to provide a toggle for a light and a dark mode. I do not know what this would look like but feel free to present proposals.

Industry/Entity Type

Continuous Integration/Testing (think LoopForge, KestrelCI)

Coding

Coded - Design and coding required

Number of Pages Required

1 page

Font styles to use
Sans Serif
Other font styles liked:
• Roboto

Colors
0054AA
0677BA
7BADD7
CADEEF
E8F1F8
FFC000
F8CF3A
FAE287
FDF2CF
FEFAEE

Requirements
Nice to have
• Light and Dark Mode

```html
<!DOCTYPE html>
<html lang="en">
<head>
<meta charset="utf-8">
<title>Lumex.CI — Portal Screens, Light and Dark</title>
<link href="https://fonts.googleapis.com/css2?family=Inter:wght@400;500;600&display=swap" rel="stylesheet">
<style>
:root{
  --board:#c6ba91;
  --navy:#14213d;
  --orange:#ff7a2b;
  --amber:#ffb000;
  --blue:#0d4fd8;
  --green:#22b35e;
  --red:#e5484d;
  --avatar:#f5b400;
}
*{box-sizing:border-box;margin:0;padding:0}
html,body{width:1200px;height:720px;overflow:hidden;background:var(--board);font-family:"Inter",Arial,sans-serif}
.board{position:relative;width:1200px;height:720px}
.slot{position:absolute;width:277px;height:177.5px;overflow:hidden}
.screen{width:571px;height:366px;transform:scale(.485);transform-origin:0 0;position:relative;overflow:hidden;
  background:var(--bg);color:var(--text);font-size:6.5px}
.light{--bg:#ffffff;--surface:#efefef;--bar:#efefef;--line:#dcdcdc;--text:#1b1b1b;--muted:#7a7a7a;--faded:#b5b5b5;--navbg:#14213d;--navtext:#ffffff;--field:#ffffff;--log:#e9eef7;--chip:#ffffff;--codenest:#14213d}
.dark{--bg:#000000;--surface:#1c1c1c;--bar:#1c1c1c;--line:#2c2c2c;--text:#ececec;--muted:#8a8a8a;--faded:#555;--navbg:#17213a;--navtext:#e8e8e8;--field:#111;--log:#000000;--chip:#111;--codenest:#16203d}
svg.i{width:7px;height:7px;fill:none;stroke:currentColor;stroke-width:2;stroke-linecap:round;stroke-linejoin:round;flex:none}

/* shared controls */
.btn{display:inline-flex;align-items:center;gap:3px;height:14px;padding:0 6px;border-radius:3px;font-size:5.5px;font-weight:500;border:1px solid var(--line);background:var(--chip);color:var(--text);white-space:nowrap}
.btn svg.i{width:6px;height:6px}
.btn.accent{background:var(--amber);border-color:var(--amber);color:#fff}
.badge{display:inline-block;padding:1px 4px;border-radius:2px;font-size:4.5px;font-weight:600;line-height:5.5px}
.badge.success{background:#dff5e7;color:#16934a}
.badge.failed{background:#fde3e3;color:#d93036}
.badge.running{background:#fff1c7;color:#b07b00}
.dark .badge.success{background:#0f3320;color:#3fd07b}
.dark .badge.failed{background:#3a1214;color:#ff6b70}
.dark .badge.running{background:#3a2c05;color:#ffc53d}
.st-ok{color:var(--green)}.st-fail{color:var(--red)}.st-run{color:var(--amber)}
.brand-dot{border-radius:50%;background:linear-gradient(135deg,#7b8aa6,#2e3a55)}

/* login */
.login .toggle{position:absolute;top:10px;right:8px}
.login .brand-dot{position:absolute;left:265px;top:39px;width:41px;height:41px}
.login h1{position:absolute;top:92px;width:100%;text-align:center;font-size:10px;font-weight:500}
.login .tagline{position:absolute;top:110px;width:100%;text-align:center;font-size:6px;color:var(--muted)}
.login .card{position:absolute;left:190px;top:132px;width:190px;height:176px;border-radius:6px;background:var(--surface)}
.login .card-title{margin-top:15px;text-align:center;font-size:6.5px}
.login .providers{margin:14px 14px 0;display:flex;flex-direction:column;gap:5px}
.login .provider{height:20px;border-radius:3px;display:flex;align-items:center;justify-content:center;gap:4px;color:#fff;font-size:5.5px;font-weight:500}
.provider.codenest{background:var(--codenest)}
.provider.repokeep{background:var(--orange)}
.provider.stackpail{background:var(--blue)}
.login hr{margin:20px 14px 0;border:0;border-top:1px solid var(--line)}
.login .terms{margin:10px 24px 0;text-align:center;font-size:5px;line-height:8px;color:var(--muted)}
.login .help{position:absolute;top:322px;width:100%;text-align:center;font-size:5px;color:var(--muted)}
.login .help span{color:var(--amber)}

/* app shell */
.app{display:flex}
.sidebar{width:108px;height:366px;background:var(--surface);border-right:1px solid var(--line);position:relative;flex:none}
.brand{display:flex;align-items:center;gap:6px;padding:10px 10px}
.brand .brand-dot{width:16px;height:16px}
.brand b{display:block;font-size:6.5px;font-weight:500}
.brand small{display:block;font-size:4.5px;color:var(--muted)}
.nav{margin-top:15px;padding:0 7px;display:flex;flex-direction:column;gap:4px}
.nav-item{height:18px;border-radius:3px;display:flex;align-items:center;gap:6px;padding:0 7px;font-size:6px;color:var(--text)}
.nav-item.filled,.nav-item.active{background:var(--navbg);color:var(--navtext)}
.nav-item.faded{color:var(--faded)}
.user{position:absolute;left:10px;bottom:12px;display:flex;align-items:center;gap:6px}
.avatar{width:13px;height:13px;border-radius:50%;background:var(--avatar);color:#fff;font-size:4.5px;display:flex;align-items:center;justify-content:center;font-weight:600}
.user b{display:block;font-size:5.5px;font-weight:500}
.user small{display:block;font-size:4.5px;color:var(--muted)}
.main{flex:1;height:366px;overflow:hidden}
.topbar{height:27px;background:var(--bar);border-bottom:1px solid var(--line);display:flex;align-items:center;padding:0 10px;gap:5px}
.topbar h2{font-size:10px;font-weight:500;margin-right:auto}
.content{padding:10px}
.muted{color:var(--muted)}
.row{display:flex;align-items:center;gap:4px}

/* projects */
.search{height:15px;border:1px solid var(--line);border-radius:3px;background:var(--field);display:flex;align-items:center;gap:4px;padding:0 5px;font-size:5px;color:var(--muted)}
.grid{margin-top:11px;display:grid;grid-template-columns:repeat(3,1fr);gap:7px}
.project{height:98px;border-radius:5px;background:var(--surface);padding:11px 10px;position:relative}
.project .name{font-size:6.5px}
.project .repo{font-size:5px;color:var(--muted);margin-top:3px}
.project .state{position:absolute;right:10px;top:10px}
.project .state svg.i{width:8px;height:8px}
.project .last{margin-top:17px;display:flex;justify-content:space-between;font-size:5px}
.project .last span:first-child{color:var(--muted)}
.project .branch{margin-top:6px;font-size:5px;color:var(--muted)}
.project .branch svg.i{width:5px;height:5px}
.project .foot{margin-top:9px;display:flex;justify-content:space-between;align-items:center;font-size:4.5px;color:var(--muted)}

/* builds */
.content.wide{padding:11px 15px}
.banner{height:39px;border-radius:5px;background:var(--surface);display:flex;align-items:center;justify-content:space-between;padding:0 10px}
.banner b{display:block;font-size:6.5px;font-weight:400}
.banner small{display:block;font-size:5px;color:var(--muted);margin-top:4px}
.build{margin-top:11px;height:57px;border-radius:5px;background:var(--surface);padding:10px 10px 0 25px;position:relative}
.build + .build{margin-top:6px}
.build .state{position:absolute;left:10px;top:11px}
.build .state svg.i{width:7px;height:7px}
.build .head{display:flex;align-items:center;gap:6px;font-size:6px}
.build .when{position:absolute;right:10px;top:10px;font-size:5px;color:var(--muted)}
.build .msg{margin-top:4px;font-size:6px}
.meta{margin-top:5px;display:grid;grid-template-columns:91px 91px 91px 1fr;font-size:5px;color:var(--muted)}
.meta span{display:flex;align-items:center;gap:3px}
.meta svg.i{width:5px;height:5px}

/* build details */
.summary{height:84px;border-radius:5px;background:var(--surface);padding:10px;position:relative}
.summary .state{position:absolute;right:10px;top:10px}
.summary .state svg.i{width:8px;height:8px}
.summary .head{display:flex;align-items:center;gap:6px;font-size:6px}
.summary .msg{margin-top:5px;font-size:6px}
.facts{margin-top:20px;display:grid;grid-template-columns:repeat(4,1fr)}
.facts span{display:flex;align-items:center;gap:3px;font-size:4.5px;color:var(--muted)}
.facts span svg.i{width:5px;height:5px}
.facts b{display:block;font-size:5px;font-weight:400;margin-top:4px}
.steps-title{margin-top:12px;font-size:7px;font-weight:500}
.step{margin-top:7px;height:74px;border-radius:5px;background:var(--surface);padding:10px 10px 0 25px;position:relative}
.step + .step{margin-top:5px}
.step .state{position:absolute;left:10px;top:10px}
.step .title{font-size:6px}
.step .dur{position:absolute;right:10px;top:10px;font-size:5px;color:var(--muted)}
.step .log{margin-top:8px;height:39px;border-radius:3px;border-left:1px solid var(--line);background:var(--log);padding:6px 7px;font-size:5px;line-height:7.5px}
</style>
</head>
<body>
<svg width="0" height="0" style="position:absolute" aria-hidden="true">
  <defs>
    <symbol id="ic-ok" viewBox="0 0 24 24"><circle cx="12" cy="12" r="10"/><path d="M8 12.5l3 3 5-6"/></symbol>
    <symbol id="ic-fail" viewBox="0 0 24 24"><circle cx="12" cy="12" r="10"/><path d="M9 9l6 6M15 9l-6 6"/></symbol>
    <symbol id="ic-run" viewBox="0 0 24 24"><circle cx="12" cy="12" r="10"/><path d="M12 7v5l3 2"/></symbol>
    <symbol id="ic-moon" viewBox="0 0 24 24"><path d="M20 14A8 8 0 1 1 10 4a6 6 0 0 0 10 10z"/></symbol>
    <symbol id="ic-sun" viewBox="0 0 24 24"><circle cx="12" cy="12" r="4"/><path d="M12 2v3M12 19v3M2 12h3M19 12h3M5 5l2 2M17 17l2 2M5 19l2-2M17 7l2-2"/></symbol>
    <symbol id="ic-grid" viewBox="0 0 24 24"><rect x="3" y="3" width="7" height="7"/><rect x="14" y="3" width="7" height="7"/><rect x="3" y="14" width="7" height="7"/><rect x="14" y="14" width="7" height="7"/></symbol>
    <symbol id="ic-folder" viewBox="0 0 24 24"><path d="M3 6h7l2 2h9v11H3z"/></symbol>
    <symbol id="ic-pulse" viewBox="0 0 24 24"><path d="M2 12h4l3-8 6 16 3-8h4"/></symbol>
    <symbol id="ic-bell" viewBox="0 0 24 24"><path d="M6 16V11a6 6 0 0 1 12 0v5l2 2H4z"/><path d="M10 21h4"/></symbol>
    <symbol id="ic-users" viewBox="0 0 24 24"><circle cx="9" cy="8" r="4"/><path d="M2 21c0-4 3-6 7-6s7 2 7 6"/><path d="M16 4a4 4 0 0 1 0 8M22 21c0-3-2-5-4-5.5"/></symbol>
    <symbol id="ic-gear" viewBox="0 0 24 24"><circle cx="12" cy="12" r="3"/><path d="M12 2v3M12 19v3M2 12h3M19 12h3M5 5l2 2M17 17l2 2M5 19l2-2M17 7l2-2"/></symbol>
    <symbol id="ic-branch" viewBox="0 0 24 24"><circle cx="6" cy="5" r="2"/><circle cx="6" cy="19" r="2"/><circle cx="18" cy="7" r="2"/><path d="M6 7v10M18 9c0 5-12 3-12 8"/></symbol>
    <symbol id="ic-commit" viewBox="0 0 24 24"><circle cx="12" cy="12" r="3"/><path d="M2 12h7M15 12h7"/></symbol>
    <symbol id="ic-user" viewBox="0 0 24 24"><circle cx="12" cy="8" r="4"/><path d="M4 21c0-4 4-6 8-6s8 2 8 6"/></symbol>
    <symbol id="ic-clock" viewBox="0 0 24 24"><circle cx="12" cy="12" r="9"/><path d="M12 7v5l3 2"/></symbol>
    <symbol id="ic-search" viewBox="0 0 24 24"><circle cx="11" cy="11" r="7"/><path d="M20 20l-4-4"/></symbol>
    <symbol id="ic-plus" viewBox="0 0 24 24"><path d="M12 5v14M5 12h14"/></symbol>
    <symbol id="ic-back" viewBox="0 0 24 24"><path d="M19 12H5M11 6l-6 6 6 6"/></symbol>
    <symbol id="ic-play" viewBox="0 0 24 24"><path d="M7 4l13 8-13 8z"/></symbol>
    <symbol id="ic-redo" viewBox="0 0 24 24"><path d="M20 12a8 8 0 1 1-3-6.2"/><path d="M20 4v5h-5"/></symbol>
    <symbol id="ic-down" viewBox="0 0 24 24"><path d="M12 3v12M7 10l5 5 5-5M4 20h16"/></symbol>
    <symbol id="ic-repo" viewBox="0 0 24 24"><rect x="4" y="3" width="16" height="18" rx="2"/><path d="M9 8h6"/></symbol>
  </defs>
</svg>

<main class="board">

<!-- ============ LIGHT ROW ============ -->

<!-- login / light -->
<div class="slot" style="left:24.3px;top:155.7px">
<section class="screen login light">
  <span class="btn toggle"><svg class="i"><use href="#ic-moon"/></svg>Dark</span>
  <div class="brand-dot"></div>
  <h1>Welcome to Lumex.CI</h1>
  <p class="tagline">Continuous Integration &amp; Testing Platform</p>
  <div class="card">
    <p class="card-title">Sign in with your account</p>
    <div class="providers">
      <div class="provider codenest"><svg class="i"><use href="#ic-repo"/></svg>Sign in with CodeNest</div>
      <div class="provider repokeep"><svg class="i"><use href="#ic-repo"/></svg>Sign in with RepoKeep</div>
      <div class="provider stackpail"><svg class="i"><use href="#ic-repo"/></svg>Sign in with Stackpail</div>
    </div>
    <hr>
    <p class="terms">By signing in, you agree to our Terms of Service and Privacy Policy</p>
  </div>
  <p class="help">Need help? <span>Contact Support</span></p>
</section>
</div>

<!-- projects / light -->
<div class="slot" style="left:317.7px;top:155.7px">
<section class="screen app light">
  <aside class="sidebar">
    <div class="brand"><div class="brand-dot"></div><div><b>Lumex.CI</b><small>CI/CD Platform</small></div></div>
    <nav class="nav">
      <div class="nav-item filled"><svg class="i"><use href="#ic-grid"/></svg>Dashboard</div>
      <div class="nav-item filled"><svg class="i"><use href="#ic-folder"/></svg>Projects</div>
      <div class="nav-item faded"><svg class="i"><use href="#ic-pulse"/></svg>Builds</div>
      <div class="nav-item filled"><svg class="i"><use href="#ic-bell"/></svg>Notifications</div>
      <div class="nav-item filled"><svg class="i"><use href="#ic-users"/></svg>Team</div>
      <div class="nav-item filled"><svg class="i"><use href="#ic-gear"/></svg>Settings</div>
    </nav>
    <div class="user"><div class="avatar">JD</div><div><b>John Doe</b><small>john@example.com</small></div></div>
  </aside>
  <div class="main">
    <header class="topbar"><h2>Projects</h2><span class="btn accent"><svg class="i"><use href="#ic-plus"/></svg>New Project</span><span class="btn"><svg class="i"><use href="#ic-moon"/></svg>Dark</span></header>
    <div class="content">
      <div class="search"><svg class="i"><use href="#ic-search"/></svg>Search projects...</div>
      <div class="grid">
        <article class="project"><div class="name">orbit-website</div><div class="repo">codenest.dev/orbit/website</div><span class="state st-ok"><svg class="i"><use href="#ic-ok"/></svg></span><div class="last"><span>Last Build:</span><span>#145</span></div><div class="branch row"><svg class="i"><use href="#ic-branch"/></svg>main</div><div class="foot"><span class="badge success">success</span><span>2 hours ago</span></div></article>
        <article class="project"><div class="name">customer-portal</div><div class="repo">repokeep.dev/orbit/portal</div><span class="state st-fail"><svg class="i"><use href="#ic-fail"/></svg></span><div class="last"><span>Last Build:</span><span>#312</span></div><div class="branch row"><svg class="i"><use href="#ic-branch"/></svg>develop</div><div class="foot"><span class="badge failed">failed</span><span>5 hours ago</span></div></article>
        <article class="project"><div class="name">api-gateway</div><div class="repo">stackpail.org/orbit/gateway</div><span class="state st-ok"><svg class="i"><use href="#ic-ok"/></svg></span><div class="last"><span>Last Build:</span><span>#89</span></div><div class="branch row"><svg class="i"><use href="#ic-branch"/></svg>main</div><div class="foot"><span class="badge success">success</span><span>1 day ago</span></div></article>
        <article class="project"><div class="name">mobile-app</div><div class="repo">codenest.dev/orbit/mobile</div><span class="state st-run"><svg class="i"><use href="#ic-run"/></svg></span><div class="last"><span>Last Build:</span><span>#256</span></div><div class="branch row"><svg class="i"><use href="#ic-branch"/></svg>feature/new-ui</div><div class="foot"><span class="badge running">running</span><span>3 days ago</span></div></article>
        <article class="project"><div class="name">analytics-dashboard</div><div class="repo">codenest.dev/orbit/analytics</div><span class="state st-ok"><svg class="i"><use href="#ic-ok"/></svg></span><div class="last"><span>Last Build:</span><span>#78</span></div><div class="branch row"><svg class="i"><use href="#ic-branch"/></svg>main</div><div class="foot"><span class="badge success">success</span><span>1 week ago</span></div></article>
        <article class="project"><div class="name">documentation-site</div><div class="repo">repokeep.dev/orbit/docs</div><span class="state st-ok"><svg class="i"><use href="#ic-ok"/></svg></span><div class="last"><span>Last Build:</span><span>#45</span></div><div class="branch row"><svg class="i"><use href="#ic-branch"/></svg>main</div><div class="foot"><span class="badge success">success</span><span>2 weeks ago</span></div></article>
      </div>
    </div>
  </div>
</section>
</div>

<!-- build history / light -->
<div class="slot" style="left:608.2px;top:155.7px">
<section class="screen app light">
  <aside class="sidebar">
    <div class="brand"><div class="brand-dot"></div><div><b>Lumex.CI</b><small>CI/CD Platform</small></div></div>
    <nav class="nav">
      <div class="nav-item"><svg class="i"><use href="#ic-grid"/></svg>Dashboard</div>
      <div class="nav-item"><svg class="i"><use href="#ic-folder"/></svg>Projects</div>
      <div class="nav-item active"><svg class="i"><use href="#ic-pulse"/></svg>Builds</div>
      <div class="nav-item faded"><svg class="i"><use href="#ic-bell"/></svg>Notifications</div>
      <div class="nav-item faded"><svg class="i"><use href="#ic-users"/></svg>Team</div>
      <div class="nav-item faded"><svg class="i"><use href="#ic-gear"/></svg>Settings</div>
    </nav>
    <div class="user"><div class="avatar">JD</div><div><b>John Doe</b><small>john@example.com</small></div></div>
  </aside>
  <div class="main">
    <header class="topbar"><h2>Build History</h2><span class="btn"><svg class="i"><use href="#ic-back"/></svg>Back to Projects</span><span class="btn"><svg class="i"><use href="#ic-moon"/></svg>Dark</span></header>
    <div class="content wide">
      <div class="banner"><div><b>orbit-website</b><small>codenest.dev/orbit/website</small></div><span class="btn accent"><svg class="i"><use href="#ic-play"/></svg>Trigger Build</span></div>
      <article class="build"><span class="state st-ok"><svg class="i"><use href="#ic-ok"/></svg></span><div class="head">Build #145 <span class="badge success">success</span></div><span class="when">2 hours ago</span><div class="msg">Update authentication flow</div><div class="meta"><span><svg class="i"><use href="#ic-branch"/></svg>main</span><span><svg class="i"><use href="#ic-commit"/></svg>a3f5c2d</span><span><svg class="i"><use href="#ic-user"/></svg>John Doe</span><span><svg class="i"><use href="#ic-clock"/></svg>3m 24s</span></div></article>
      <article class="build"><span class="state st-fail"><svg class="i"><use href="#ic-fail"/></svg></span><div class="head">Build #144 <span class="badge failed">failed</span></div><span class="when">5 hours ago</span><div class="msg">Add new dashboard components</div><div class="meta"><span><svg class="i"><use href="#ic-branch"/></svg>develop</span><span><svg class="i"><use href="#ic-commit"/></svg>b7e9f1a</span><span><svg class="i"><use href="#ic-user"/></svg>Jane Smith</span><span><svg class="i"><use href="#ic-clock"/></svg>2m 15s</span></div></article>
      <article class="build"><span class="state st-ok"><svg class="i"><use href="#ic-ok"/></svg></span><div class="head">Build #143 <span class="badge success">success</span></div><span class="when">8 hours ago</span><div class="msg">Fix API endpoint issues</div><div class="meta"><span><svg class="i"><use href="#ic-branch"/></svg>main</span><span><svg class="i"><use href="#ic-commit"/></svg>c1d4e8b</span><span><svg class="i"><use href="#ic-user"/></svg>Mike Johnson</span><span><svg class="i"><use href="#ic-clock"/></svg>4m 12s</span></div></article>
      <article class="build"><span class="state st-run"><svg class="i"><use href="#ic-run"/></svg></span><div class="head">Build #142 <span class="badge running">running</span></div><span class="when">12 hours ago</span><div class="msg">Implement dark mode toggle</div><div class="meta"><span><svg class="i"><use href="#ic-branch"/></svg>feature/new-ui</span><span><svg class="i"><use href="#ic-commit"/></svg>d9a2c7e</span><span><svg class="i"><use href="#ic-user"/></svg>Sarah Williams</span><span><svg class="i"><use href="#ic-clock"/></svg>1m 45s</span></div></article>
      <article class="build"><span class="state st-ok"><svg class="i"><use href="#ic-ok"/></svg></span><div class="head">Build #141 <span class="badge success">success</span></div><span class="when">1 day ago</span><div class="msg">Update dependencies</div></article>
    </div>
  </div>
</section>
</div>

<!-- build details / light -->
<div class="slot" style="left:898.7px;top:155.7px">
<section class="screen app light">
  <aside class="sidebar">
    <div class="brand"><div class="brand-dot"></div><div><b>Lumex.CI</b><small>CI/CD Platform</small></div></div>
    <nav class="nav">
      <div class="nav-item"><svg class="i"><use href="#ic-grid"/></svg>Dashboard</div>
      <div class="nav-item"><svg class="i"><use href="#ic-folder"/></svg>Projects</div>
      <div class="nav-item active"><svg class="i"><use href="#ic-pulse"/></svg>Builds</div>
      <div class="nav-item faded"><svg class="i"><use href="#ic-bell"/></svg>Notifications</div>
      <div class="nav-item faded"><svg class="i"><use href="#ic-users"/></svg>Team</div>
      <div class="nav-item faded"><svg class="i"><use href="#ic-gear"/></svg>Settings</div>
    </nav>
    <div class="user"><div class="avatar">JD</div><div><b>John Doe</b><small>john@example.com</small></div></div>
  </aside>
  <div class="main">
    <header class="topbar"><h2>Build Details</h2><span class="btn"><svg class="i"><use href="#ic-down"/></svg>Download Logs</span><span class="btn"><svg class="i"><use href="#ic-redo"/></svg>Rebuild</span><span class="btn"><svg class="i"><use href="#ic-back"/></svg>Back</span><span class="btn"><svg class="i"><use href="#ic-moon"/></svg>Dark</span></header>
    <div class="content wide">
      <div class="summary"><span class="state st-ok"><svg class="i"><use href="#ic-ok"/></svg></span><div class="head">Build #145 <span class="badge success">success</span></div><div class="msg">Update authentication flow</div>
        <div class="facts"><div><span><svg class="i"><use href="#ic-branch"/></svg>Branch</span><b>main</b></div><div><span><svg class="i"><use href="#ic-commit"/></svg>Commit</span><b>a3f5c2d</b></div><div><span><svg class="i"><use href="#ic-user"/></svg>Author</span><b>John Doe</b></div><div><span><svg class="i"><use href="#ic-clock"/></svg>Duration</span><b>3m 24s</b></div></div></div>
      <h3 class="steps-title">Build Steps</h3>
      <article class="step"><span class="state st-ok"><svg class="i"><use href="#ic-ok"/></svg></span><div class="title">Initialize Build Environment</div><span class="dur">12s</span><div class="log">Setting up Runlet 18.x<br>Installing dependencies...<br>Environment ready</div></article>
      <article class="step"><span class="state st-ok"><svg class="i"><use href="#ic-ok"/></svg></span><div class="title">Clone Repository</div><span class="dur">8s</span><div class="log">Cloning into /workspace...<br>Checking out commit a3f5c2d<br>Repository cloned successfully</div></article>
      <article class="step"><span class="state st-ok"><svg class="i"><use href="#ic-ok"/></svg></span><div class="title">Install Dependencies</div><span class="dur">45s</span><div class="log">Running pkgr install...<br>Added 243 packages in 43s<br>Dependencies installed</div></article>
    </div>
  </div>
</section>
</div>

<!-- ============ DARK ROW ============ -->

<!-- login / dark -->
<div class="slot" style="left:24.3px;top:386.3px">
<section class="screen login dark">
  <span class="btn toggle"><svg class="i st-run"><use href="#ic-sun"/></svg>Light</span>
  <div class="brand-dot"></div>
  <h1>Welcome to Lumex.CI</h1>
  <p class="tagline">Continuous Integration &amp; Testing Platform</p>
  <div class="card">
    <p class="card-title">Sign in with your account</p>
    <div class="providers">
      <div class="provider codenest"><svg class="i"><use href="#ic-repo"/></svg>Sign in with CodeNest</div>
      <div class="provider repokeep"><svg class="i"><use href="#ic-repo"/></svg>Sign in with RepoKeep</div>
      <div class="provider stackpail"><svg class="i"><use href="#ic-repo"/></svg>Sign in with Stackpail</div>
    </div>
    <hr>
    <p class="terms">By signing in, you agree to our Terms of Service and Privacy Policy</p>
  </div>
  <p class="help">Need help? <span>Contact Support</span></p>
</section>
</div>

<!-- projects / dark -->
<div class="slot" style="left:317.7px;top:386.3px">
<section class="screen app dark">
  <aside class="sidebar">
    <div class="brand"><div class="brand-dot"></div><div><b>Lumex.CI</b><small>CI/CD Platform</small></div></div>
    <nav class="nav">
      <div class="nav-item filled"><svg class="i"><use href="#ic-grid"/></svg>Dashboard</div>
      <div class="nav-item filled"><svg class="i"><use href="#ic-folder"/></svg>Projects</div>
      <div class="nav-item faded"><svg class="i"><use href="#ic-pulse"/></svg>Builds</div>
      <div class="nav-item filled"><svg class="i"><use href="#ic-bell"/></svg>Notifications</div>
      <div class="nav-item filled"><svg class="i"><use href="#ic-users"/></svg>Team</div>
      <div class="nav-item filled"><svg class="i"><use href="#ic-gear"/></svg>Settings</div>
    </nav>
    <div class="user"><div class="avatar">JD</div><div><b>John Doe</b><small>john@example.com</small></div></div>
  </aside>
  <div class="main">
    <header class="topbar"><h2>Projects</h2><span class="btn accent"><svg class="i"><use href="#ic-plus"/></svg>New Project</span><span class="btn"><svg class="i st-run"><use href="#ic-sun"/></svg>Light</span></header>
    <div class="content">
      <div class="search"><svg class="i"><use href="#ic-search"/></svg>Search projects...</div>
      <div class="grid">
        <article class="project"><div class="name">orbit-website</div><div class="repo">codenest.dev/orbit/website</div><span class="state st-ok"><svg class="i"><use href="#ic-ok"/></svg></span><div class="last"><span>Last Build:</span><span>#145</span></div><div class="branch row"><svg class="i"><use href="#ic-branch"/></svg>main</div><div class="foot"><span class="badge success">success</span><span>2 hours ago</span></div></article>
        <article class="project"><div class="name">customer-portal</div><div class="repo">repokeep.dev/orbit/portal</div><span class="state st-fail"><svg class="i"><use href="#ic-fail"/></svg></span><div class="last"><span>Last Build:</span><span>#312</span></div><div class="branch row"><svg class="i"><use href="#ic-branch"/></svg>develop</div><div class="foot"><span class="badge failed">failed</span><span>5 hours ago</span></div></article>
        <article class="project"><div class="name">api-gateway</div><div class="repo">stackpail.org/orbit/gateway</div><span class="state st-ok"><svg class="i"><use href="#ic-ok"/></svg></span><div class="last"><span>Last Build:</span><span>#89</span></div><div class="branch row"><svg class="i"><use href="#ic-branch"/></svg>main</div><div class="foot"><span class="badge success">success</span><span>1 day ago</span></div></article>
        <article class="project"><div class="name">mobile-app</div><div class="repo">codenest.dev/orbit/mobile</div><span class="state st-run"><svg class="i"><use href="#ic-run"/></svg></span><div class="last"><span>Last Build:</span><span>#256</span></div><div class="branch row"><svg class="i"><use href="#ic-branch"/></svg>feature/new-ui</div><div class="foot"><span class="badge running">running</span><span>3 days ago</span></div></article>
        <article class="project"><div class="name">analytics-dashboard</div><div class="repo">codenest.dev/orbit/analytics</div><span class="state st-ok"><svg class="i"><use href="#ic-ok"/></svg></span><div class="last"><span>Last Build:</span><span>#78</span></div><div class="branch row"><svg class="i"><use href="#ic-branch"/></svg>main</div><div class="foot"><span class="badge success">success</span><span>1 week ago</span></div></article>
        <article class="project"><div class="name">documentation-site</div><div class="repo">repokeep.dev/orbit/docs</div><span class="state st-ok"><svg class="i"><use href="#ic-ok"/></svg></span><div class="last"><span>Last Build:</span><span>#45</span></div><div class="branch row"><svg class="i"><use href="#ic-branch"/></svg>main</div><div class="foot"><span class="badge success">success</span><span>2 weeks ago</span></div></article>
      </div>
    </div>
  </div>
</section>
</div>

<!-- build history / dark -->
<div class="slot" style="left:608.2px;top:386.3px">
<section class="screen app dark">
  <aside class="sidebar">
    <div class="brand"><div class="brand-dot"></div><div><b>Lumex.CI</b><small>CI/CD Platform</small></div></div>
    <nav class="nav">
      <div class="nav-item"><svg class="i"><use href="#ic-grid"/></svg>Dashboard</div>
      <div class="nav-item"><svg class="i"><use href="#ic-folder"/></svg>Projects</div>
      <div class="nav-item active"><svg class="i"><use href="#ic-pulse"/></svg>Builds</div>
      <div class="nav-item faded"><svg class="i"><use href="#ic-bell"/></svg>Notifications</div>
      <div class="nav-item faded"><svg class="i"><use href="#ic-users"/></svg>Team</div>
      <div class="nav-item faded"><svg class="i"><use href="#ic-gear"/></svg>Settings</div>
    </nav>
    <div class="user"><div class="avatar">JD</div><div><b>John Doe</b><small>john@example.com</small></div></div>
  </aside>
  <div class="main">
    <header class="topbar"><h2>Build History</h2><span class="btn"><svg class="i"><use href="#ic-back"/></svg>Back to Projects</span><span class="btn"><svg class="i st-run"><use href="#ic-sun"/></svg>Light</span></header>
    <div class="content wide">
      <div class="banner"><div><b>orbit-website</b><small>codenest.dev/orbit/website</small></div><span class="btn accent"><svg class="i"><use href="#ic-play"/></svg>Trigger Build</span></div>
      <article class="build"><span class="state st-ok"><svg class="i"><use href="#ic-ok"/></svg></span><div class="head">Build #145 <span class="badge success">success</span></div><span class="when">2 hours ago</span><div class="msg">Update authentication flow</div><div class="meta"><span><svg class="i"><use href="#ic-branch"/></svg>main</span><span><svg class="i"><use href="#ic-commit"/></svg>a3f5c2d</span><span><svg class="i"><use href="#ic-user"/></svg>John Doe</span><span><svg class="i"><use href="#ic-clock"/></svg>3m 24s</span></div></article>
      <article class="build"><span class="state st-fail"><svg class="i"><use href="#ic-fail"/></svg></span><div class="head">Build #144 <span class="badge failed">failed</span></div><span class="when">5 hours ago</span><div class="msg">Add new dashboard components</div><div class="meta"><span><svg class="i"><use href="#ic-branch"/></svg>develop</span><span><svg class="i"><use href="#ic-commit"/></svg>b7e9f1a</span><span><svg class="i"><use href="#ic-user"/></svg>Jane Smith</span><span><svg class="i"><use href="#ic-clock"/></svg>2m 15s</span></div></article>
      <article class="build"><span class="state st-ok"><svg class="i"><use href="#ic-ok"/></svg></span><div class="head">Build #143 <span class="badge success">success</span></div><span class="when">8 hours ago</span><div class="msg">Fix API endpoint issues</div><div class="meta"><span><svg class="i"><use href="#ic-branch"/></svg>main</span><span><svg class="i"><use href="#ic-commit"/></svg>c1d4e8b</span><span><svg class="i"><use href="#ic-user"/></svg>Mike Johnson</span><span><svg class="i"><use href="#ic-clock"/></svg>4m 12s</span></div></article>
      <article class="build"><span class="state st-run"><svg class="i"><use href="#ic-run"/></svg></span><div class="head">Build #142 <span class="badge running">running</span></div><span class="when">12 hours ago</span><div class="msg">Implement dark mode toggle</div><div class="meta"><span><svg class="i"><use href="#ic-branch"/></svg>feature/new-ui</span><span><svg class="i"><use href="#ic-commit"/></svg>d9a2c7e</span><span><svg class="i"><use href="#ic-user"/></svg>Sarah Williams</span><span><svg class="i"><use href="#ic-clock"/></svg>1m 45s</span></div></article>
      <article class="build"><span class="state st-ok"><svg class="i"><use href="#ic-ok"/></svg></span><div class="head">Build #141 <span class="badge success">success</span></div><span class="when">1 day ago</span><div class="msg">Update dependencies</div></article>
    </div>
  </div>
</section>
</div>

<!-- build details / dark -->
<div class="slot" style="left:898.7px;top:386.3px">
<section class="screen app dark">
  <aside class="sidebar">
    <div class="brand"><div class="brand-dot"></div><div><b>Lumex.CI</b><small>CI/CD Platform</small></div></div>
    <nav class="nav">
      <div class="nav-item"><svg class="i"><use href="#ic-grid"/></svg>Dashboard</div>
      <div class="nav-item"><svg class="i"><use href="#ic-folder"/></svg>Projects</div>
      <div class="nav-item active"><svg class="i"><use href="#ic-pulse"/></svg>Builds</div>
      <div class="nav-item faded"><svg class="i"><use href="#ic-bell"/></svg>Notifications</div>
      <div class="nav-item faded"><svg class="i"><use href="#ic-users"/></svg>Team</div>
      <div class="nav-item faded"><svg class="i"><use href="#ic-gear"/></svg>Settings</div>
    </nav>
    <div class="user"><div class="avatar">JD</div><div><b>John Doe</b><small>john@example.com</small></div></div>
  </aside>
  <div class="main">
    <header class="topbar"><h2>Build Details</h2><span class="btn"><svg class="i"><use href="#ic-down"/></svg>Download Logs</span><span class="btn"><svg class="i"><use href="#ic-redo"/></svg>Rebuild</span><span class="btn"><svg class="i"><use href="#ic-back"/></svg>Back</span><span class="btn"><svg class="i st-run"><use href="#ic-sun"/></svg>Light</span></header>
    <div class="content wide">
      <div class="summary"><span class="state st-ok"><svg class="i"><use href="#ic-ok"/></svg></span><div class="head">Build #145 <span class="badge success">success</span></div><div class="msg">Update authentication flow</div>
        <div class="facts"><div><span><svg class="i"><use href="#ic-branch"/></svg>Branch</span><b>main</b></div><div><span><svg class="i"><use href="#ic-commit"/></svg>Commit</span><b>a3f5c2d</b></div><div><span><svg class="i"><use href="#ic-user"/></svg>Author</span><b>John Doe</b></div><div><span><svg class="i"><use href="#ic-clock"/></svg>Duration</span><b>3m 24s</b></div></div></div>
      <h3 class="steps-title">Build Steps</h3>
      <article class="step"><span class="state st-ok"><svg class="i"><use href="#ic-ok"/></svg></span><div class="title">Initialize Build Environment</div><span class="dur">12s</span><div class="log">Setting up Runlet 18.x<br>Installing dependencies...<br>Environment ready</div></article>
      <article class="step"><span class="state st-ok"><svg class="i"><use href="#ic-ok"/></svg></span><div class="title">Clone Repository</div><span class="dur">8s</span><div class="log">Cloning into /workspace...<br>Checking out commit a3f5c2d<br>Repository cloned successfully</div></article>
      <article class="step"><span class="state st-ok"><svg class="i"><use href="#ic-ok"/></svg></span><div class="title">Install Dependencies</div><span class="dur">45s</span><div class="log">Running pkgr install...<br>Added 243 packages in 43s<br>Dependencies installed</div></article>
    </div>
  </div>
</section>
</div>

</main>
</body>
</html>
```